" O escritório de advocacia atua de forma estratégica e personalizada, oferecendo assessoria jurídica completa com foco na excelência técnica, na ética profissional e na construção de soluções eficazes para seus clientes. O atendimento é conduzido diretamente pelos sócios, garantindo proximidade, confiança e alto nível de especialização em cada demanda. Cada caso é analisado de maneira individualizada, com abordagem analítica, planejamento jurídico preciso e comunicação clara. O escritório combina tradição jurídica e visão contemporânea, utilizando métodos atualizados, organização eficiente e atuação responsável para entregar segurança jurídica e resultados consistentes. "

```html
<!DOCTYPE html>
<html lang="pt-BR">
<head>
<meta charset="UTF-8">
<title>Envelope saco – Moreira &amp; Castro Advogados</title>
<link href="https://fonts.googleapis.com/css2?family=Montserrat:wght@500;600&display=swap" rel="stylesheet">
<style>
  :root{
    --navy:#13294b;
    --navy-line:#1d3760;
    --paper:#ffffff;
    --name-grey:#8c8c8c;
    --backdrop:#e9e7e4;
    --light-text:#ffffff;
  }
  *{margin:0;padding:0;box-sizing:border-box}
  html,body{width:1200px;height:1200px;overflow:hidden;background:var(--backdrop)}
  .sheet{position:relative;width:1200px;height:1200px}
  .envelope{position:absolute;top:211px;width:466px;height:720px;box-shadow:0 6px 18px rgba(0,0,0,.18)}
  .envelope--front{left:139px;background:var(--paper)}
  .envelope--back{left:629px;background:var(--navy)}
  .envelope__flap{position:absolute;left:0;top:0;width:100%;height:30px}
  .envelope__band{position:absolute;left:0;bottom:0;width:100%;height:19px;background:var(--navy)}
  .envelope__seams{position:absolute;left:0;top:0;width:100%;height:120px}
  .firm-name{position:absolute;left:0;width:100%;text-align:center;font-family:'Montserrat',sans-serif;font-weight:500;white-space:nowrap}
  .envelope--front .firm-name{top:390px;font-size:25px;color:var(--name-grey)}
  .envelope--back .firm-name{top:650px;font-size:12px;color:var(--light-text)}
  .envelope__address{position:absolute;left:0;width:100%;top:680px;text-align:center;font-family:'Montserrat',sans-serif;font-weight:600;font-size:9.5px;color:var(--light-text);letter-spacing:.02em;white-space:nowrap}
</style>
</head>
<body>
<main class="sheet">
  <section class="envelope envelope--front" aria-label="Frente do envelope">
    <svg class="envelope__flap" viewBox="0 0 466 30" preserveAspectRatio="none" aria-hidden="true">
      <polygon points="0,0 466,0 466,30 0,30" fill="var(--navy)"/>
      <polygon points="0,0 14,30 0,30" fill="var(--paper)"/>
      <polygon points="466,0 452,30 466,30" fill="var(--paper)"/>
    </svg>
    <p class="firm-name">Moreira &amp; Castro Advogados</p>
    <div class="envelope__band"></div>
  </section>

  <section class="envelope envelope--back" aria-label="Verso do envelope">
    <svg class="envelope__seams" viewBox="0 0 466 120" preserveAspectRatio="none" aria-hidden="true">
      <line x1="0" y1="28" x2="466" y2="28" stroke="var(--navy-line)" stroke-width="1.5"/>
      <line x1="14" y1="28" x2="0" y2="0" stroke="var(--navy-line)" stroke-width="1.5"/>
      <line x1="452" y1="28" x2="466" y2="0" stroke="var(--navy-line)" stroke-width="1.5"/>
    </svg>
    <p class="firm-name">Moreira &amp; Castro Advogados</p>
    <p class="envelope__address">Rua das Palmeiras, 48 - Sala 305 - Centro - Rio de Janeiro | RJ</p>
  </section>
</main>
</body>
</html>
```